Real Estate Business card design

Company Name: Tamarind Holdings, LLC
subtitle: We pay cash for houses!
Daniel Whitcombe
Managing Director
555-214-0963
Dan@TamarindHoldingsLLC.example
www.TamarindHoldingsLLC.example

We pay referral fees for Seller and Buyer leads.

Back:
We offer referral fees for Seller and Buyer leads that close.

Please contact Hal at 555-214-0963 with your referrals or to learn more about the referral program!

I am open to different color options but I am going for a classic, elegant, clean, and professional look. Please use logo as a reference.

Target Market(s)

People selling their homes and people in the market for buying homes.

Contact Information for Business Card

please see project description

Font styles to use
Serif
Sans Serif
Script

Requirements
Must have
• must have my logo in it
Nice to have
• I like cards that are split down the middle but please come up with a few mock ups. Open to any color scheme.

```html
<!DOCTYPE html>
<html lang="en">
<head>
<meta charset="utf-8">
<title>Tamarind Holdings, LLC – Business Card</title>
<link rel="stylesheet" href="https://fonts.googleapis.com/css2?family=Roboto:wght@300;400;500&display=swap">
<style>
  :root {
    --stage: #3a3b3e;
    --card-front: #f4f4f4;
    --card-back: #474f5b;
    --navy: #1b2a5a;
    --ink: #2e2e30;
    --gold: #c79c6e;
    --white: #ffffff;
  }
  * { margin: 0; padding: 0; box-sizing: border-box; }
  html, body {
    width: 1200px; height: 900px; overflow: hidden;
    background: var(--stage);
    font-family: "Roboto", sans-serif;
  }
  .canvas {
    position: relative; width: 1200px; height: 900px;
  }
  .card {
    position: absolute; left: 250px; width: 700px; height: 400px;
    border-radius: 34px; overflow: hidden;
    box-shadow: 0 18px 40px rgba(0,0,0,0.45);
  }
  .card--front { top: 40px; background: var(--card-front); }
  .card--back  { top: 470px; background: var(--card-back); }

  /* Front */
  .brand {
    position: absolute; left: 300px; top: 52px; width: 300px; text-align: center;
  }
  .brand__row { display: flex; align-items: center; justify-content: center; gap: 10px; }
  .brand__mark { width: 14px; height: 14px; background: var(--gold); }
  .brand__name {
    font-weight: 500; font-size: 26px; color: var(--ink); letter-spacing: 0.2px;
  }
  .brand__tagline {
    margin-top: 8px; font-size: 15px; font-weight: 300; color: var(--gold);
  }
  .rule {
    position: absolute; left: 250px; right: 0; top: 196px; height: 3px; background: var(--navy);
  }
  .person { position: absolute; left: 60px; top: 150px; }
  .person__name { font-size: 34px; font-weight: 500; color: var(--ink); }
  .person__title { font-size: 19px; font-weight: 400; color: var(--navy); margin-top: 14px; }
  .contact { position: absolute; left: 385px; top: 156px; }
  .contact__heading { font-size: 22px; font-weight: 500; color: var(--navy); }
  .contact__list { list-style: none; margin-top: 22px; font-size: 13.5px; font-weight: 300; color: var(--ink); line-height: 1.75; }
  .social { display: flex; gap: 10px; margin-top: 14px; margin-left: 30px; }
  .social__item { width: 24px; height: 24px; border-radius: 6px; background: var(--navy); }

  /* Back */
  .back-brand {
    position: absolute; left: 0; right: 0; top: 150px;
    display: flex; align-items: center; justify-content: center; gap: 16px;
  }
  .back-brand__mark { width: 26px; height: 26px; background: var(--gold); }
  .back-brand__name { font-size: 44px; font-weight: 500; color: var(--white); }
  .referral {
    position: absolute; left: 0; right: 0; top: 262px; text-align: center;
    color: var(--white); font-weight: 300; font-size: 15px; line-height: 1.5;
  }
  .referral__phone { font-size: 22px; }
</style>
</head>
<body>
<main class="canvas">
  <section class="card card--front" aria-label="Business card front">
    <div class="brand">
      <div class="brand__row">
        <span class="brand__mark"></span>
        <span class="brand__name">Tamarind Holdings, LLC</span>
      </div>
      <p class="brand__tagline">We pay cash for houses!</p>
    </div>
    <div class="rule"></div>
    <div class="person">
      <h1 class="person__name">Daniel Whitcombe</h1>
      <p class="person__title">Managing Director</p>
    </div>
    <div class="contact">
      <h2 class="contact__heading">Contact Details</h2>
      <ul class="contact__list">
        <li>Email: Dan@TamarindHoldingsLLC.example</li>
        <li>Mobile: 555-214-0963</li>
        <li>www.TamarindHoldingsLLC.example</li>
      </ul>
      <div class="social" aria-label="Social media links">
        <span class="social__item"></span>
        <span class="social__item"></span>
        <span class="social__item"></span>
        <span class="social__item"></span>
      </div>
    </div>
  </section>

  <section class="card card--back" aria-label="Business card back">
    <div class="back-brand">
      <span class="back-brand__mark"></span>
      <span class="back-brand__name">Tamarind Holdings, LLC</span>
    </div>
    <p class="referral">
      Please contact Hal at <span class="referral__phone">555-214-0963</span> with your referrals<br>
      or to learn more about the referral program!
    </p>
  </section>
</main>
</body>
</html>
```